Criação de Kit Layout de Posts para Redes Sociais (Facebook, Instagram e etc) para Advocacia e Direito
" Prestamos assessoria para os clientes saberem sua situação atual, perante a Previdência Social, e fazemos um planejamento previdenciário, com acompanhamento até a concessão do benefício pretendido, seja pela via administrativa, seja pela via judicial. Assim, realizamos contagem de tempo de contribuição, simulação de valor de benefício, planejamento previdenciário, requerimento administrativo e ajuizamento de ação judicial, tudo para o fim de obter a concessão de Aposentadoria, revisão de benefício, Auxílio-Doença, Auxílio-Acidente, Salário-Maternidade, Pensão por morte, Auxílio-Reclusão e Benefício Assistencial. "

```html
<!DOCTYPE html>
<html lang="pt-BR">
<head>
<meta charset="UTF-8">
<title>Reforma da previdência: entenda as Regras de Transição</title>
<link href="https://fonts.googleapis.com/css2?family=Nunito+Sans:wght@500;600;700&display=swap" rel="stylesheet">
<style>
  :root {
    --navy: #0f2447;
    --navy-deep: #0a1b38;
    --gold: #c9a86a;
    --white: #ffffff;
    --sky-top: #b7c3cf;
    --sky-glow: #fbf3df;
    --sky-warm: #e9cf9e;
    --ground: #a88758;
    --ink: #142a4e;
  }
  * { margin: 0; padding: 0; box-sizing: border-box; }
  html, body { width: 1200px; height: 1200px; overflow: hidden; }
  body { font-family: "Nunito Sans", Arial, sans-serif; }

  .post {
    position: relative;
    width: 1200px;
    height: 1200px;
    overflow: hidden;
  }

  .backdrop {
    position: absolute;
    inset: 0;
    background:
      radial-gradient(ellipse 55% 40% at 78% 58%, rgba(255,252,240,0.95) 0%, rgba(255,248,228,0.6) 40%, rgba(255,248,228,0) 75%),
      linear-gradient(90deg, rgba(80,95,120,0.45) 0%, rgba(120,125,140,0.15) 40%, rgba(255,255,255,0) 70%),
      linear-gradient(180deg, var(--sky-top) 0%, #dcdcd6 25%, var(--sky-glow) 50%, var(--sky-warm) 72%, var(--ground) 100%);
  }

  .top-band {
    position: absolute;
    left: 0;
    top: 96px;
    width: 1160px;
    height: 156px;
    background: linear-gradient(90deg, var(--navy-deep) 0%, var(--navy) 80%, rgba(15,36,71,0.85) 100%);
  }

  .brand-box {
    position: absolute;
    left: 84px;
    top: 36px;
    width: 384px;
    height: 384px;
    background: var(--navy);
    border: 4px solid var(--gold);
    display: flex;
    flex-direction: column;
    justify-content: center;
    padding: 0 36px 0 40px;
  }

  .brand-row {
    display: flex;
    align-items: center;
    gap: 18px;
  }

  .brand-mark {
    flex: none;
    width: 52px;
    height: 52px;
    background: var(--gold);
  }

  .brand-name {
    color: var(--white);
    font-weight: 600;
    font-size: 31px;
    line-height: 1.12;
    letter-spacing: 0.5px;
    text-transform: uppercase;
  }

  .brand-tagline {
    margin-top: 12px;
    padding-left: 70px;
    color: var(--white);
    font-weight: 600;
    font-size: 11.5px;
    letter-spacing: 2.6px;
    text-transform: uppercase;
  }

  .headline {
    position: absolute;
    left: 0;
    top: 560px;
    width: 1200px;
    text-align: center;
    color: var(--ink);
  }

  .headline-kicker {
    font-weight: 600;
    font-size: 48px;
    line-height: 1.2;
  }

  .headline-main {
    margin-top: 28px;
    font-weight: 700;
    font-size: 62px;
    line-height: 1.2;
  }
</style>
</head>
<body>
  <main class="post">
    <div class="backdrop" role="img" aria-label="Fotografia de um céu ao pôr do sol com a silhueta de uma pessoa subindo uma escada no canto inferior esquerdo"></div>

    <div class="top-band"></div>

    <div class="brand-box">
      <div class="brand-row">
        <span class="brand-mark"></span>
        <span class="brand-name">Valmont<br>Ribeiro</span>
      </div>
      <p class="brand-tagline">Sociedade de Advocacia</p>
    </div>

    <h1 class="headline">
      <span class="headline-kicker" style="display:block">Reforma da previdência:</span>
      <span class="headline-main" style="display:block">entenda as Regras de Transição</span>
    </h1>
  </main>
</body>
</html>
```